Empower our Electric Journey on the Web

We need a new website that can promote our services. Our three services that we offer are:
- Management of e-mobility charging stations
- Management of energy purchases
- Leasing of E-Mobility charging stations
- Energy billing of private electricity meters
The website should work responsively on PC, tablet and smartphone. In general, a simple navigation and an appealing design should be in the foreground. The website should give the customer the possibility to request , based pm a preset chexkbox chart and to get in contact with us.
Our logo works on black and white background.
Our slogan is:
Empower Your Electric Journey with Velmor Mobility
The 4 Pages should be the following:
Main Page, with info about us, why choose us,
2nd; services; what we sell and what are our services
3rd; Contact us, request an offer
4th, References about costumers and Work we already did, in the future we would like to integrate a Blog Post in this section in stead of references.

Target Market(s)

Landlords, Homeowners, Homeowner Associations

Industry/Entity Type

EV Chargers / E-Mobility

Coding

Coded - Design and coding required

Number of Pages Required

4 page

Requirements
Nice to have
• Pop up to our mailchimp newsletter subscription

```html
<!DOCTYPE html>
<html lang="en">
<head>
<meta charset="utf-8">
<title>Velmor Mobility</title>
<link rel="stylesheet" href="https://fonts.googleapis.com/css2?family=Poppins:wght@400;500;600;700&display=swap">
<style>
:root{
  --green:#4cbb3a;
  --green-bright:#5fd04a;
  --green-dark:#3aa42c;
  --green-soft:#eef8ee;
  --ink:#111111;
  --text:#2b2b2b;
  --muted:#555555;
  --white:#ffffff;
  --grey-bg:#e9ece9;
}
*{margin:0;padding:0;box-sizing:border-box}
html,body{width:1200px;height:4441px;overflow:hidden}
body{position:relative;font-family:'Poppins',sans-serif;color:var(--text);background:var(--white)}
.abs{position:absolute}
svg.layer{position:absolute;left:0;top:0}

/* header */
.brand{left:114px;top:12px;display:flex;align-items:center;gap:10px;font-size:26px;font-weight:700;color:var(--green);letter-spacing:1px;line-height:1}
.brand .dot{width:22px;height:22px;border-radius:50%;background:var(--green)}
.nav{left:467px;top:26px;display:flex;gap:32px;font-size:12px;font-weight:500;color:var(--ink)}
.nav .active{border-bottom:2px solid var(--ink);padding-bottom:10px}
.head-cta{left:995px;top:22px;font-size:15px;font-weight:600;color:var(--ink);display:flex;align-items:center;gap:8px}

/* hero */
.hero-title{left:181px;top:195px;width:480px;font-size:34px;line-height:50px;font-weight:600;color:var(--white);text-transform:uppercase}
.hero-text{left:181px;top:343px;width:440px;font-size:14.5px;line-height:26px;color:#f0f0f0}
.btn{display:flex;align-items:center;justify-content:center;gap:8px;font-size:12.5px;font-weight:600;text-transform:uppercase}
.btn-hero{left:178px;top:414px;width:174px;height:43px;background:var(--white);color:var(--ink);clip-path:polygon(0 0,100% 0,86% 100%,0 100%)}

/* section headings */
.eyebrow{font-size:13px;font-weight:600;color:var(--green-dark);text-transform:uppercase}
.heading{font-size:35px;font-weight:600;color:var(--ink);text-transform:uppercase;line-height:1.1}
.center{left:0;width:1200px;text-align:center}
.rule{height:3px;width:82px;background:var(--green)}

.btn-outline{border:1.5px solid var(--green);color:var(--green-dark);background:var(--white);clip-path:polygon(0 0,100% 0,88% 100%,0 100%)}
.btn-green{background:var(--green);color:var(--white);clip-path:polygon(0 0,100% 0,88% 100%,0 100%)}

/* about */
.about-copy{left:631px;top:955px;width:465px;font-size:15px;line-height:26px;color:var(--text)}
.about-copy strong{color:var(--ink);font-weight:600}

/* services */
.service{width:260px}
.service h3{font-size:17px;font-weight:600;color:var(--green-dark);line-height:26px}
.service p{font-size:13px;line-height:26px;color:var(--muted);margin-top:4px}
.right-align{text-align:right}
.ring{width:80px;height:80px;border:2.5px solid var(--green);border-radius:50%;background:var(--white);display:flex;align-items:center;justify-content:center}
.hub{left:469px;top:1535px;width:258px;height:258px;border-radius:50%;background:var(--white);display:flex;align-items:center;justify-content:center;font-size:26px;font-weight:700;color:var(--green);letter-spacing:1px}

/* why */
.why-copy{left:162px;top:2182px;width:430px;font-size:16px;line-height:26px}
.why-copy strong{color:var(--ink);font-weight:600}
.why-list{left:162px;top:2298px;list-style:none;font-size:13px;color:var(--ink)}
.why-list li{display:flex;align-items:center;gap:12px;height:35px}
.why-list li::before{content:"";width:7px;height:7px;border-right:2px solid var(--green);border-bottom:2px solid var(--green);transform:rotate(-45deg)}

/* blogs */
.blog-photo{width:419px;height:252px}
.blog-card{width:371px;height:199px;background:var(--white);clip-path:polygon(0 0,100% 0,90% 100%,0 100%);padding:20px 30px}
.blog-card .date{font-size:14px;font-weight:600;color:var(--green-dark)}
.blog-card h4{font-size:17px;line-height:23px;font-weight:600;color:var(--ink);margin-top:4px}
.blog-card p{font-size:12px;line-height:21px;color:var(--muted);margin-top:8px}
.blog-card .more{font-size:12px;font-weight:600;color:var(--green-dark);margin-top:10px;display:flex;gap:8px;align-items:center}

/* contact */
.touch-title{left:228px;top:3447px;font-size:22px;font-weight:500;color:var(--white)}
.touch-item{left:272px;font-size:14px;line-height:20px;color:var(--white);text-transform:uppercase}
.touch-icon{left:224px}
.form-title{left:555px;top:3443px;font-size:22px;font-weight:500;color:var(--white)}
.field{left:567px;width:416px;font-size:14px;color:var(--white);border-bottom:1px solid rgba(255,255,255,.7);padding-bottom:8px}
.btn-form{left:559px;top:3745px;width:162px;height:41px;background:var(--white);color:var(--green-dark);clip-path:polygon(0 0,100% 0,86% 100%,0 100%)}

/* footer */
.foot-head{font-size:14px;font-weight:500;color:var(--ink);text-transform:uppercase}
.foot-list{list-style:none;font-size:11.5px;color:#333}
.foot-list li{height:26px}
.foot-services li{height:22px}
.divider{width:2px;background:#555;opacity:.6}
.social{width:28px;height:28px;border:1.5px solid #333;border-radius:50%}
.foot-contact{font-size:11.5px;line-height:18px;color:#333}
.foot-icon{width:28px;height:28px;border-radius:50%;background:var(--green)}
.copyright{left:0;top:4399px;width:1200px;text-align:center;font-size:11px;color:#333}
</style>
</head>
<body>

<!-- background shapes -->
<svg class="layer" width="1200" height="4441" viewBox="0 0 1200 4441">
  <defs>
    <linearGradient id="heroFill" x1="0" y1="0" x2="1" y2="1">
      <stop offset="0" stop-color="#3f4a33"/>
      <stop offset=".45" stop-color="#7b6a58"/>
      <stop offset="1" stop-color="#5b5347"/>
    </linearGradient>
    <linearGradient id="blogBg" x1="0" y1="0" x2="0" y2="1">
      <stop offset="0" stop-color="#eef6ee"/>
      <stop offset="1" stop-color="#dfe3df"/>
    </linearGradient>
    <linearGradient id="footBg" x1="0" y1="0" x2="0" y2="1">
      <stop offset="0" stop-color="#f1f2f1"/>
      <stop offset="1" stop-color="#dcdedc"/>
    </linearGradient>
  </defs>

  <!-- header -->
  <polygon points="995,0 1200,0 1200,69 957,69" fill="var(--green)"/>
  <polygon points="957,69 995,0 985,0 947,69" fill="var(--ink)"/>

  <!-- hero -->
  <g role="img" aria-label="Photo of wall-mounted EV charging units outside a house at dusk">
    <polygon points="0,69 1200,69 1200,552 607,715 0,552" fill="url(#heroFill)"/>
  </g>
  <polyline points="0,566 607,718 1200,552" fill="none" stroke="var(--green)" stroke-width="6"/>
  <line x1="607" y1="718" x2="607" y2="770" stroke="#333" stroke-width="1.5"/>
  <circle cx="607" cy="771" r="8" fill="var(--green)"/>

  <!-- about image -->
  <polyline points="560,860 560,1250 190,1250" fill="none" stroke="var(--green)" stroke-width="5"/>
  <g role="img" aria-label="Photo of a woman using her phone beside a charging electric car">
    <polygon points="186,775 552,860 552,1242 186,1200" fill="#8e9aa8"/>
  </g>

  <!-- services band -->
  <rect x="0" y="1345" width="1200" height="627" fill="var(--green-soft)"/>

  <!-- why image -->
  <rect x="640" y="2180" width="26" height="26" fill="#bfe8b6"/>
  <rect x="972" y="2485" width="20" height="32" fill="#bfe8b6"/>
  <g role="img" aria-label="Photo of an electric car charging in front of a modern garage">
    <rect x="681" y="2146" width="351" height="335" fill="#b9a7b8"/>
    <rect x="619" y="2200" width="352" height="340" fill="#6f7076"/>
    <rect x="972" y="2185" width="60" height="296" fill="#2c3438"/>
  </g>

  <!-- blogs band -->
  <rect x="0" y="2614" width="1200" height="627" fill="url(#blogBg)"/>
  <g role="img" aria-label="Photo of charging posts along a tree-lined car park at night">
    <rect x="164" y="2781" width="419" height="252" fill="#4e5a46"/>
  </g>
  <g role="img" aria-label="Photo of charging stations in front of a parked car">
    <rect x="619" y="2781" width="419" height="252" fill="#9c9a98"/>
  </g>
  <path d="M95 2907 H60 M74 2894 L60 2907 L74 2920" fill="none" stroke="#333" stroke-width="2.5"/>
  <path d="M1105 2907 H1140 M1126 2894 L1140 2907 L1126 2920" fill="none" stroke="#333" stroke-width="2.5"/>

  <!-- contact box -->
  <rect x="174" y="3400" width="338" height="426" fill="var(--green)"/>
  <polygon points="512,3400 1064,3400 982,3826 512,3826" fill="var(--green-bright)"/>
  <line x1="1066" y1="3400" x2="984" y2="3826" stroke="var(--ink)" stroke-width="5"/>

  <!-- footer -->
  <polygon points="0,4043 607,3875 1200,4043 1200,4441 0,4441" fill="url(#footBg)"/>
  <polyline points="0,4043 607,3875 1200,4043" fill="none" stroke="var(--green)" stroke-width="6"/>
  <line x1="0" y1="4379" x2="1200" y2="4379" stroke="#999" stroke-width="1"/>
</svg>

<!-- header -->
<div class="abs brand"><span class="dot"></span>VELMOR MOBILITY</div>
<nav class="abs nav">
  <span class="active">HOME</span><span>ABOUT US</span><span>WHY CHOOSE US</span><span>OUR SERVICES</span><span>BLOGS</span>
</nav>
<div class="abs head-cta">
  <svg width="18" height="18" viewBox="0 0 24 24"><path d="M6.6 10.8a15 15 0 0 0 6.6 6.6l2.2-2.2c.3-.3.7-.4 1-.2 1.1.4 2.3.6 3.6.6.6 0 1 .4 1 1V20c0 .6-.4 1-1 1A17 17 0 0 1 3 4c0-.6.4-1 1-1h3.5c.6 0 1 .4 1 1 0 1.3.2 2.5.6 3.6.1.3 0 .7-.2 1z" fill="var(--ink)"/></svg>
  CONTACT US
</div>

<!-- hero -->
<h1 class="abs hero-title">Empower your electric journey with Velmor Mobility</h1>
<p class="abs hero-text">Lorem Ipsum has been the industry's standard dummy text ever since the 1500s, when an unknown printer</p>
<div class="abs btn btn-hero">Contact us</div>

<!-- about -->
<div class="abs eyebrow" style="left:634px;top:861px">Who we are</div>
<h2 class="abs heading" style="left:631px;top:886px">About us</h2>
<div class="abs rule" style="left:631px;top:935px"></div>
<p class="abs about-copy"><strong>Lorem Ipsum has been the industry's standard dummy text ever since the 1500s, when an unknown.</strong> printer took a galley of type and scrambled it to make a type specimen book. It has survived not only five centuries, but also the leap into electronic typesetting, remaining essentially unchanged. It was popularised in the 1960s with the release of Letraset sheets containing Lorem Ipsum passages, and more recently with desktop publishing</p>
<div class="abs btn btn-outline" style="left:631px;top:1178px;width:175px;height:43px">Learn more
  <svg width="16" height="10" viewBox="0 0 16 10"><path d="M0 5h14M10 1l4 4-4 4" fill="none" stroke="var(--green-dark)" stroke-width="1.5"/></svg></div>

<!-- services -->
<div class="abs eyebrow center" style="top:1387px">What we offer</div>
<h2 class="abs heading center" style="top:1410px">Our services</h2>
<div class="abs rule" style="left:559px;top:1460px"></div>

<div class="abs hub">VELMOR</div>

<div class="abs service right-align" style="left:116px;top:1527px">
  <h3>Management of e-mobility charging stations</h3>
  <p>Lorem Ipsum has been the industry's standard dummy text ever.</p>
</div>
<div class="abs ring" style="left:386px;top:1524px">
  <svg width="36" height="36" viewBox="0 0 24 24" fill="none" stroke="var(--green)" stroke-width="1.5"><rect x="5" y="3" width="9" height="18" rx="1"/><path d="M10 8l-2 4h3l-2 4M14 10h2a2 2 0 0 1 2 2v5a1.5 1.5 0 0 0 3 0V8"/></svg>
</div>

<div class="abs service right-align" style="left:116px;top:1720px">
  <h3>Management of energy purchases</h3>
  <p>Lorem Ipsum has been the industry's standard dummy text ever.</p>
</div>
<div class="abs ring" style="left:386px;top:1718px">
  <svg width="36" height="36" viewBox="0 0 24 24" fill="none" stroke="var(--green)" stroke-width="1.5"><path d="M4 4h16M6 4v4h12V4M12 8v4M7 12h10v8H7zM10 15h4M10 18h4"/></svg>
</div>

<div class="abs ring" style="left:732px;top:1524px">
  <svg width="36" height="36" viewBox="0 0 24 24" fill="none" stroke="var(--green)" stroke-width="1.5"><rect x="4" y="4" width="10" height="12" rx="1"/><path d="M9 7l-2 3h3l-2 3M3 20h18M14 9h3v7"/></svg>
</div>
<div class="abs service" style="left:824px;top:1524px">
  <h3>Leasing of E-Mobility charging stations</h3>
  <p>Lorem Ipsum has been the industry's standard dummy text ever.</p>
</div>

<div class="abs ring" style="left:732px;top:1718px">
  <svg width="36" height="36" viewBox="0 0 24 24" fill="none" stroke="var(--green)" stroke-width="1.5"><circle cx="12" cy="10" r="6"/><path d="M12 6l-2 4h4l-2 4M9 16v4h6v-4"/></svg>
</div>
<div class="abs service" style="left:824px;top:1717px">
  <h3>Energy billing of private electricity meters</h3>
  <p>Lorem Ipsum has been the industry's standard dummy text ever.</p>
</div>

<div class="abs btn btn-green" style="left:514px;top:1867px;width:174px;height:43px">Learn more
  <svg width="16" height="10" viewBox="0 0 16 10"><path d="M0 5h14M10 1l4 4-4 4" fill="none" stroke="#fff" stroke-width="1.5"/></svg></div>

<!-- why choose -->
<div class="abs eyebrow center" style="top:2026px">Why choose us</div>
<h2 class="abs heading center" style="top:2049px">Why choose us</h2>

<p class="abs why-copy"><strong>Lorem Ipsum has been the industry's standard dummy text ever since the 1500s.</strong> when an unknown printer took a galley of type and scrambled it to make a type specimen book.</p>
<ul class="abs why-list">
  <li>Energy billing of private electricity meters</li>
  <li>Management of energy purchases</li>
  <li>Leasing of E-Mobility charging stations</li>
  <li>Management of e-mobility charging stations</li>
</ul>
<div class="abs btn btn-outline" style="left:162px;top:2446px;width:175px;height:43px">Learn more
  <svg width="16" height="10" viewBox="0 0 16 10"><path d="M0 5h14M10 1l4 4-4 4" fill="none" stroke="var(--green-dark)" stroke-width="1.5"/></svg></div>

<!-- blogs -->
<div class="abs eyebrow center" style="top:2667px">Blogs</div>
<h2 class="abs heading center" style="top:2691px">Latest blogs</h2>

<article class="abs blog-card" style="left:181px;top:2977px">
  <div class="date">11 MAR 2023</div>
  <h4>Lorem Ipsum has been the industry's standard dummy text</h4>
  <p>Lorem Ipsum has been the industry's standard dummy text ever since the 1500s.</p>
  <div class="more">READ MORE <svg width="16" height="10" viewBox="0 0 16 10"><path d="M0 5h14M10 1l4 4-4 4" fill="none" stroke="var(--green-dark)" stroke-width="1.5"/></svg></div>
</article>
<article class="abs blog-card" style="left:636px;top:2977px">
  <div class="date">10 FEB 2023</div>
  <h4>Lorem Ipsum has been the industry's standard dummy text</h4>
  <p>Lorem Ipsum has been the industry's standard dummy text ever since the 1500s.</p>
  <div class="more">READ MORE <svg width="16" height="10" viewBox="0 0 16 10"><path d="M0 5h14M10 1l4 4-4 4" fill="none" stroke="var(--green-dark)" stroke-width="1.5"/></svg></div>
</article>

<!-- contact -->
<div class="abs eyebrow center" style="top:3290px">Contact</div>
<h2 class="abs heading center" style="top:3313px">Contact us</h2>

<div class="abs touch-title">GET IN TOUCH</div>
<svg class="abs touch-icon" style="top:3506px" width="32" height="32" viewBox="0 0 24 24" fill="none" stroke="#fff" stroke-width="1.3"><path d="M12 21s-6-6-6-11a6 6 0 0 1 12 0c0 5-6 11-6 11z"/><circle cx="12" cy="10" r="2.2"/><ellipse cx="12" cy="21" rx="5" ry="1.2"/></svg>
<div class="abs touch-item" style="top:3503px">Address<br><span style="text-transform:none">B- Crest Way, Fairview<br>WA 6099 Perth – USA</span></div>
<svg class="abs touch-icon" style="top:3590px" width="32" height="32" viewBox="0 0 24 24" fill="none" stroke="#fff" stroke-width="1.3"><path d="M6.6 10.8a15 15 0 0 0 6.6 6.6l2.2-2.2c.3-.3.7-.4 1-.2 1.1.4 2.3.6 3.6.6.6 0 1 .4 1 1V20c0 .6-.4 1-1 1A17 17 0 0 1 3 4c0-.6.4-1 1-1h3.5c.6 0 1 .4 1 1 0 1.3.2 2.5.6 3.6.1.3 0 .7-.2 1z"/></svg>
<div class="abs touch-item" style="top:3596px">Phone number<br>+100 555 0142</div>
<svg class="abs touch-icon" style="top:3686px" width="32" height="26" viewBox="0 0 24 18" fill="none" stroke="#fff" stroke-width="1.3"><rect x="1" y="1" width="22" height="16"/><path d="M1 1l11 9 11-9M1 17l8-7M23 17l-8-7"/></svg>
<div class="abs touch-item" style="top:3684px">Email us<br>info@velmormobility.com</div>

<div class="abs form-title">LEAVE US A MESAGE</div>
<div class="abs field" style="top:3494px">Name *</div>
<div class="abs field" style="top:3539px">E-mail *</div>
<div class="abs field" style="top:3594px">Phone Number *</div>
<div class="abs field" style="top:3643px;height:82px">Message</div>
<div class="abs btn btn-form">Learn more
  <svg width="16" height="10" viewBox="0 0 16 10"><path d="M0 5h14M10 1l4 4-4 4" fill="none" stroke="var(--green-dark)" stroke-width="1.5"/></svg></div>

<!-- footer -->
<div class="abs brand" style="left:114px;top:4142px;font-size:21px"><span class="dot" style="width:18px;height:18px"></span>VELMOR MOBILITY</div>
<div class="abs" style="left:112px;top:4194px;display:flex;gap:4px">
  <span class="social"></span><span class="social"></span><span class="social"></span><span class="social"></span>
</div>

<div class="abs divider" style="left:328px;top:4120px;height:198px"></div>
<div class="abs foot-head" style="left:357px;top:4122px">Navigation</div>
<ul class="abs foot-list" style="left:357px;top:4156px">
  <li>Home</li><li>About Us</li><li>Tours</li><li>Bookings</li><li>Contact Us</li>
</ul>

<div class="abs divider" style="left:510px;top:4120px;height:198px"></div>
<div class="abs foot-head" style="left:531px;top:4120px">Contact us</div>
<div class="abs foot-icon" style="left:527px;top:4158px"></div>
<div class="abs foot-contact" style="left:567px;top:4155px">Phone<br>100-555-0142</div>
<div class="abs foot-icon" style="left:527px;top:4214px"></div>
<div class="abs foot-contact" style="left:567px;top:4211px">Email<br>info@velmormobility.com</div>
<div class="abs foot-icon" style="left:527px;top:4270px"></div>
<div class="abs foot-contact" style="left:567px;top:4267px">Address<br>218 Harlow Street, Brightmoor VIC 3999</div>

<div class="abs divider" style="left:814px;top:4120px;height:198px"></div>
<div class="abs foot-head" style="left:838px;top:4122px">Services</div>
<ul class="abs foot-list foot-services" style="left:842px;top:4156px">
  <li>Management of e-mobility charging stations</li>
  <li>Management of energy purchases</li>
  <li>Leasing of E-Mobility charging stations</li>
  <li>Energy billing of private electricity meters</li>
</ul>

<div class="abs copyright">© 2023 VELMOR MOBILITY. ALL RIGHTS RESERVED</div>

</body>
</html>
```